Catalogue design for vbl ugg boots and slippers

We need a catalogue developed for our Licensed VBL Ugg Boots and Ugg Slippers. There are 16 teams in the VBL (Coastal Netball Circuit competition in Australia) and each team has an Adult Unisex designs, A childrens design and a slipper design.
We have our own logo. The catalogue will be used by our sales reps to showcase the range to prospective retailers.
There should be photos of the product (each team individually) We have 3 photos of the adult boot, 2 photos of the kids boots and 3 photos of the slippers for each team which need to be incorporated. We also need a size availability table for each item that needs to be included.
A front page design is required as well as a table of content, about is page and a description page.
Information about us can be found at www.fernlowboots.com.au
All the images can be found at this dropbox link
https://www.filecrate-example.net/sh/pq83xr5tmw0zd/BBHRtk92vQ7e-LmYs4nTfJw?dl=0

Reason: Need more designs to come through.

Font styles to use
Serif

Requirements
Must have
• Images of all the boots and slippers and tables for size availability

```html
<!DOCTYPE html>
<html lang="en">
<head>
<meta charset="utf-8">
<title>Fernlow Catalog 2017 – Cover</title>
<link rel="stylesheet" href="https://fonts.googleapis.com/css2?family=Open+Sans:wght@700&family=Oswald:wght@500;700&display=swap">
<style>
  :root {
    --page-bg: #ffffff;
    --label-grey: #9b9b9b;
    --navy: #062a78;
    --royal: #2466b2;
    --amber: #fab01a;
    --amber-deep: #f77700;
    --brand-yellow: #fbb617;
    --year-blue: #1f5fae;
    --white: #ffffff;
  }
  html, body {
    margin: 0;
    width: 1200px;
    height: 1200px;
    overflow: hidden;
    background: var(--page-bg);
  }
  .sheet {
    position: relative;
    width: 1200px;
    height: 1200px;
  }
  .section-label {
    position: absolute;
    left: 84px;
    top: 130px;
    margin: 0;
    font-family: "Open Sans", Arial, sans-serif;
    font-weight: 700;
    font-size: 46px;
    line-height: 1;
    color: var(--label-grey);
    letter-spacing: -0.5px;
  }
  .cover {
    position: absolute;
    left: 81px;
    top: 228px;
    width: 1027px;
    height: 726px;
    background: var(--white);
    box-shadow: 0 0 22px rgba(0, 0, 0, 0.12);
  }
  .cover svg { display: block; }
  .brand-name {
    font-family: "Oswald", "Arial Narrow", sans-serif;
    font-weight: 700;
    fill: var(--brand-yellow);
  }
  .catalog-title {
    font-family: "Oswald", "Arial Narrow", sans-serif;
    font-weight: 500;
    fill: var(--white);
  }
  .catalog-year {
    font-family: "Oswald", "Arial Narrow", sans-serif;
    font-weight: 500;
    fill: var(--year-blue);
  }
</style>
</head>
<body>
<main class="sheet">
  <h1 class="section-label">COVER</h1>

  <section class="cover" aria-label="Catalog cover">
    <svg width="1027" height="726" viewBox="0 0 1027 726" xmlns="http://www.w3.org/2000/svg">
      <defs>
        <linearGradient id="sky-band" x1="0" y1="0" x2="0" y2="1">
          <stop offset="0" stop-color="var(--navy)"/>
          <stop offset="0.12" stop-color="#072c7c"/>
          <stop offset="0.7" stop-color="var(--royal)"/>
          <stop offset="1" stop-color="var(--royal)"/>
        </linearGradient>
        <linearGradient id="amber-band" x1="0.55" y1="0.2" x2="0.95" y2="1">
          <stop offset="0" stop-color="var(--amber)"/>
          <stop offset="0.55" stop-color="var(--amber)"/>
          <stop offset="1" stop-color="var(--amber-deep)"/>
        </linearGradient>
      </defs>

      <polygon class="sky-band" points="0,0 909,0 769,526 0,526" fill="url(#sky-band)"/>

      <polygon class="amber-band" points="0,538 955,538 905,726 0,726" fill="url(#amber-band)"/>
      <polygon class="amber-edge" points="934,554 948,554 901,726 887,726" fill="#fbb23a" opacity="0.45"/>

      <text class="brand-name" x="925" y="518" text-anchor="end" font-size="150"
            textLength="420" lengthAdjust="spacingAndGlyphs">FERNLOW</text>

      <text class="catalog-title" x="519" y="638" font-size="80"
            textLength="198" lengthAdjust="spacingAndGlyphs">CATALOG</text>
      <text class="catalog-year" x="741" y="638" font-size="50"
            textLength="62" lengthAdjust="spacingAndGlyphs">2017</text>
    </svg>
  </section>
</main>
</body>
</html>
```